Bruntel general construction

We need an website that are similar to these websites:
https://www.morvexa.com/en/
https://dulnari.com/company/

but with a tweak. Do not copy the entire website but atleast similar and yet better than them.

For reference this our current website.
https://bruntel.ph/

For the winning Designer please help us with the migration from our old website to the new redesign website.

```html
<!DOCTYPE html>
<html lang="en">
<head>
<meta charset="utf-8">
<title>Bruntel — Environmental EPC Services</title>
<link href="https://fonts.googleapis.com/css2?family=Outfit:wght@300;400;500;600&display=swap" rel="stylesheet">
<style>
:root{
  --orange:#f5821f;
  --orange-soft:#f08a45;
  --blue:#1e8bc8;
  --ink:#1c1c1c;
  --body:#555;
  --cream:#fff4e6;
  --dark:#14232b;
  --footer:#2a2a2a;
}
*{box-sizing:border-box;margin:0;padding:0}
html,body{width:1200px;height:3841px;overflow:hidden}
body{font-family:'Outfit',sans-serif;color:var(--ink);background:#fff;position:relative}
section,header,footer{position:relative;width:1200px;overflow:hidden}
.abs{position:absolute}
.btn{display:inline-block;background:var(--orange);color:#fff;font-size:11px;text-transform:uppercase;border-radius:16px;padding:9px 15px;letter-spacing:.2px}
.accent{width:56px;height:3px;background:var(--orange);border-radius:2px}
.more{color:var(--orange);font-size:9px;font-weight:600;text-transform:uppercase}

/* hero */
.hero{height:586px;background:linear-gradient(180deg,#1d2d33 0%,#24343a 40%,#3a3a33 70%,#121a1e 100%)}
.brand{left:200px;top:18px;display:flex;flex-direction:column;align-items:center;gap:6px}
.brand .mark{width:34px;height:34px;border-radius:50%;background:var(--orange)}
.brand span{color:var(--blue);font-weight:600;font-size:14px;letter-spacing:.5px}
.nav{left:472px;top:52px;display:flex;gap:30px;font-size:10.5px;color:#fff;text-transform:uppercase}
.nav .on{color:var(--orange);border-bottom:1px solid var(--orange);padding-bottom:3px}
.hero .cta{left:906px;top:45px}
.hero h1{left:200px;width:800px;top:219px;text-align:center;color:#fff;font-weight:500;font-size:39px;line-height:44px}
.hero .btns{left:0;width:1200px;top:412px;display:flex;justify-content:center;gap:12px}
.round{width:30px;height:30px;border-radius:50%;background:var(--orange);display:flex;align-items:center;justify-content:center}

/* about */
.about{height:577px}
.about .drop{left:232px;top:50px}
.about .text{left:609px;top:90px;width:390px}
.about h2{font-size:28px;font-weight:500}
.about h2 b{color:var(--blue);font-weight:500}
.about p{font-size:11.5px;line-height:20px;color:var(--body);font-weight:300;margin-top:18px}
.about .accent{margin-top:8px}

/* expertise */
.expertise{height:569px;background:var(--cream)}
.section-head{text-align:center}
.section-head h2{font-size:29px;font-weight:500}
.section-head .accent{margin:8px auto 0}
.section-head p{font-size:11.5px;color:var(--body);line-height:20px;margin-top:14px;font-weight:300}
.expertise .section-head{position:absolute;left:300px;width:600px;top:60px}
.cards{left:200px;display:flex;gap:20px}
.card{width:253px;background:#fff;border-radius:8px;overflow:hidden}
.card .ph{height:170px}
.card .bd{padding:16px 15px}
.card h3{color:var(--orange);font-size:11.5px;font-weight:500;margin-bottom:8px}
.card p{font-size:9.5px;line-height:15px;color:var(--body);font-weight:300;min-height:75px}
.expertise .cards{top:173px}
.expertise .card{height:320px}
.sel{border-bottom:2px solid var(--orange)}

/* mission */
.mission{height:464px}
.mission h3{font-size:19px;font-weight:500}
.mission p{font-size:11.5px;line-height:20px;color:var(--body);font-weight:300;margin-top:20px}
.mission .accent{margin-top:8px}
.pic{border-radius:6px}

/* banner */
.banner{height:305px;background:linear-gradient(180deg,#22313a 0%,#3a3330 55%,#5a3a22 80%,#1c1a18 100%)}
.banner h2{left:225px;width:750px;top:100px;text-align:center;color:#fff;font-size:28px;font-weight:500;line-height:34px}

/* team */
.team{height:533px}
.team .section-head{position:absolute;left:300px;width:600px;top:52px}
.member{width:389px;text-align:center}
.member .ph{height:268px}
.member h4{font-size:15px;font-weight:500;margin-top:16px}
.member small{display:block;color:var(--orange);font-size:8.5px;text-transform:uppercase;margin-top:6px;font-weight:500}

/* news */
.news{height:518px}
.news h2{font-size:29px;font-weight:500}
.news .card{height:321px;background:#fdf6f0}
.news .card .ph{position:relative}
.tag{position:absolute;left:10px;top:10px;background:var(--orange);color:#fff;font-size:7.5px;padding:4px 9px;border-radius:9px;text-transform:uppercase}
.news .card h3{color:var(--ink);font-size:11px;line-height:15px}

/* footer */
footer{height:289px;background:var(--footer);color:#ddd}
footer h5{font-size:14px;font-weight:500;color:#fff}
.col p{font-size:9.5px;line-height:14px;color:#ccc;display:flex;gap:10px;margin-top:14px;font-weight:300}
.col svg{flex:none}
.badge{width:88px;height:67px;background:#fff;border-radius:2px;display:flex;align-items:center;justify-content:center}
.badge i{width:44px;height:44px;border-radius:50%;border:2px solid #c9cfd8;display:block}
.social{width:30px;height:30px;border-radius:50%;border:1px solid var(--orange)}
.copy{left:0;width:1200px;top:3815px;text-align:center;font-size:9.5px;color:#ddd}
</style>
</head>
<body>

<header class="hero">
  <div class="abs brand"><div class="mark"></div><span>BRUNTEL</span></div>
  <nav class="abs nav"><span class="on">Home</span><span>About Us</span><span>Our Services</span><span>Our Team</span><span>News &amp; Media</span></nav>
  <a class="abs btn cta">Contact Us</a>
  <h1 class="abs">We Assist In The Advancement Of An Environment Friendly Society By Providing Our Services To World-Renowned Environmental EPC Companies.</h1>
  <div class="abs btns"><a class="btn">Contact Us</a><a class="btn">View Our Services</a></div>
  <div class="abs round" style="left:1084px;top:316px"><svg width="12" height="12" viewBox="0 0 12 12"><path d="M2 6h8M7 3l3 3-3 3" stroke="#fff" fill="none" stroke-width="1.3"/></svg></div>
  <svg class="abs" style="left:594px;top:528px" width="12" height="28" viewBox="0 0 12 28"><path d="M6 0v26M1 21l5 5 5-5" stroke="#fff" fill="none" stroke-width="1"/></svg>
</header>

<section class="about">
  <svg class="abs drop" width="320" height="462" viewBox="0 0 320 462" role="img" aria-label="Engineer in hard hat walking through a refinery at sunset">
    <defs><linearGradient id="dropFill" x1="0" y1="0" x2="0" y2="1"><stop offset="0" stop-color="#7c8a94"/><stop offset=".55" stop-color="#c98a4a"/><stop offset="1" stop-color="#3b3a36"/></linearGradient></defs>
    <path d="M160 4 C200 90 316 210 316 300 A156 156 0 0 1 4 300 C4 210 120 90 160 4Z" fill="url(#dropFill)" stroke="var(--orange)" stroke-width="4"/>
  </svg>
  <div class="abs text">
    <h2>We At <b>BRUNTEL</b></h2>
    <div class="accent"></div>
    <p>With More Than Four Years Of Established Business Relationships With Various Blue Chip Clients And Major Construction Companies, We At Bruntel Can Provide A Wide Range Of Services To The Oil, Gas, Energy, And Environmental Sectors. While We Aim For Sustainability And Profitability In All Our Projects, We Strive To Protect The Environment And The Health And Safety Of Our People And The Communities Where We Operate.</p>
    <p>We Deliver What We Promise And In Doing So Exceed Our Client's Expectations. We Are Able To Achieve This By Providing A Host Of Services To Different Industries From One Source, Reducing Our Client's Overheads In The Process.</p>
    <p>Bruntel Continues To Support The Oil, Gas, Power, Water, And Environmental Industries Throughout Asia And Is Expanding Its Services To Become A Leader In These Fields.</p>
    <a class="btn" style="margin-top:18px">Read More</a>
  </div>
</section>

<section class="expertise">
  <div class="section-head">
    <h2>Our Expertise</h2>
    <p style="margin-top:24px">Our Ability To Deliver A Quality Product Has Given Us The Reputation To Position Ourselves As A Leading Contractor In The Sectors And Industries That We Serve</p>
  </div>
  <div class="abs cards">
    <article class="card"><div class="ph" role="img" aria-label="Hands passing a young seedling" style="background:linear-gradient(160deg,#8fa57a,#d8c9b6)"></div><div class="bd"><h3>Environmental Protection &amp; Management</h3><p>We Have In-House Expertise For The Processing Of Both Municipal And Industrial Solid Wastes By Adopting The Latest Technologies. These Wastes Can Be Converted To Energy In The Form Of Electrical Power.</p><span class="more">Read More →</span></div></article>
    <article class="card sel"><div class="ph" role="img" aria-label="Power transmission towers at dusk" style="background:linear-gradient(180deg,#2f5fa0,#e6a43a)"></div><div class="bd"><h3>Power Generation</h3><p>We Are Experienced In The Refurbishments Of Utility, Steam Raising Plant, The Repair And Maintenance Of Ancillary Equipment From Valves To Pumps And Our Experiences In Plant Shutdown R&amp;M Programs.</p><span class="more">Read More →</span></div></article>
    <article class="card"><div class="ph" role="img" aria-label="Water treatment tanks beside a reservoir" style="background:linear-gradient(180deg,#8fa46a,#5d88b4)"></div><div class="bd"><h3>Water Treatment</h3><p>We Have In-House Expertise For The Onstruction Of Sewage Water Treatment Plants (SWTP) And Utility Desalination Plants For The Conversion Of Seawater To Potable Water.</p><span class="more">Read More →</span></div></article>
  </div>
  <div class="abs round" style="left:984px;top:317px"><svg width="12" height="12" viewBox="0 0 12 12"><path d="M2 6h8M7 3l3 3-3 3" stroke="#fff" fill="none" stroke-width="1.3"/></svg></div>
</section>

<section class="mission">
  <div class="abs" style="left:201px;top:80px;width:390px">
    <h3>Our Mission</h3><div class="accent"></div>
    <p>To Exceed Our Client's Expectations By Demonstratively Adding Value To Their Business By Delivering World-Class Quality Work, Providing Solutions To Critical Challenges , And Making A Significant Impact On Wider Society And The Environment.</p>
  </div>
  <div class="abs pic" style="left:610px;top:52px;width:389px;height:169px;background:linear-gradient(135deg,#1f3a78,#c07a3a 60%,#1b2440)" role="img" aria-label="Industrial plant lit at night"></div>
  <div class="abs pic" style="left:200px;top:248px;width:390px;height:167px;background:linear-gradient(135deg,#8a9a9c,#2f5a5e 60%,#1f2e30)" role="img" aria-label="Steel processing plant with pipes and stacks"></div>
  <div class="abs" style="left:610px;top:274px;width:390px">
    <h3>Our Vision</h3><div class="accent"></div>
    <p>To Become A World Leader That Actively Contributes To The Global Dialogue On Resource Protection, Management, And Sustainability By Providing World-Class Training And Services That Help With The Positive Growth Of Our Clientele, And Our People.</p>
  </div>
</section>

<section class="banner" role="img" aria-label="Offshore platform silhouette at sunset">
  <h2 class="abs">Outstanding Safety, Environmental Awareness, And World-Class Quality Defines The Way We Work.</h2>
  <a class="abs btn" style="left:547px;top:180px">Contact Us</a>
</section>

<section class="team">
  <div class="section-head">
    <h2>Our Team</h2><div class="accent"></div>
    <p>With Over 50 Years Of Combined Industry Experience, Our Senior Management Team Possess The Most Competent Skills And Abilities That Ensure Bruntel's Legacy And Success.</p>
  </div>
  <div class="abs member" style="left:200px;top:165px"><div class="ph pic" role="img" aria-label="Portrait of the country manager" style="background:linear-gradient(180deg,#4d6a72,#6a8a96)"></div><h4>Renato Valmores MBA PMP</h4><small>Country Manager</small></div>
  <div class="abs member" style="left:610px;top:165px"><div class="ph pic" role="img" aria-label="Portrait of the managing director" style="background:var(--orange-soft);display:flex;align-items:center;justify-content:center;color:#fff;font-size:10px">VIEW BIO ↗</div><h4>Owen Carrick</h4><small>Managing Director</small></div>
  <div class="abs" style="left:200px;top:532px;width:800px;height:1px;background:#e6e6e6"></div>
</section>

<section class="news">
  <h2 class="abs" style="left:200px;top:44px">Latest News</h2>
  <div class="abs accent" style="left:200px;top:88px"></div>
  <a class="abs btn" style="left:892px;top:50px">View All News</a>
  <div class="abs cards" style="top:113px">
    <article class="card"><div class="ph" role="img" aria-label="Hazy city skyline behind a public garden" style="background:linear-gradient(180deg,#c8ccc8,#8a9088)"><span class="tag">October 16, 2017</span></div><div class="bd"><h3>Environmental Protection Industry A Job Creator</h3><p>A Very Different Approach Is Emerging Between Australia And China's Treatment Of Jobs And Industries Providing Goods And Services For Environmental Protection.</p><span class="more">Read More →</span></div></article>
    <article class="card sel"><div class="ph" role="img" aria-label="Two engineers reviewing plans on site" style="background:linear-gradient(180deg,#b9c4cc,#5f7a96)"><span class="tag">October 16, 2017</span></div><div class="bd"><h3>The Next Corporate Imperative: Climate Change Risk Management</h3><p>The Extreme Weather Events Witnessed This Summer In North America, In Which Hurricanes Harvey, Irma, And Maria Devastated Areas Of The Caribbean And Southeastern US In...</p><span class="more">Read More →</span></div></article>
    <article class="card"><div class="ph" role="img" aria-label="Sustainability sign on a blue surface" style="background:linear-gradient(160deg,#2e4a6a,#7fa0c0)"><span class="tag">October 16, 2017</span></div><div class="bd"><h3>Retail Giants And Investors Talk Risk And Supply Chains</h3><p>This Week I Saw A Continuation Of A Couple Of Trends: Courting Investor Interest And Retailer/ Manufacturer Sustainability Initiatives.</p><span class="more">Read More →</span></div></article>
  </div>
  <div class="abs round" style="left:984px;top:287px"><svg width="12" height="12" viewBox="0 0 12 12"><path d="M2 6h8M7 3l3 3-3 3" stroke="#fff" fill="none" stroke-width="1.3"/></svg></div>
</section>

<footer>
  <div class="abs brand" style="left:200px;top:58px"><div class="mark" style="width:60px;height:60px"></div><span style="font-size:18px">BRUNTEL</span></div>
  <div class="abs" style="left:200px;top:204px;display:flex;align-items:center;gap:10px;font-size:12px;color:#fff">Follow Us: <span class="social"></span><span class="social"></span></div>
  <div class="abs col" style="left:404px;top:50px;width:180px">
    <h5>Head Office</h5>
    <p><svg width="10" height="12" viewBox="0 0 10 12"><path d="M5 11S1 7 1 4.5a4 4 0 0 1 8 0C9 7 5 11 5 11z" stroke="var(--orange)" fill="none"/><circle cx="5" cy="4.5" r="1.3" fill="var(--orange)"/></svg>14 Mabini Ridge Rd. Brgy. Lanton Talisay Heights, Cavite Philippines 4120</p>
    <p><svg width="11" height="11" viewBox="0 0 11 11"><path d="M2 1l2 .2.8 2.3-1.2 1a6 6 0 0 0 3 3l1-1.2 2.3.8.1 2C7 10 1 4 2 1z" stroke="var(--orange)" fill="none"/></svg><u>+63 (0) 46 555-0147</u></p>
    <p><svg width="12" height="10" viewBox="0 0 12 10"><rect x=".5" y=".5" width="11" height="9" stroke="var(--orange)" fill="none"/><path d="M.5 .5L6 5l5.5-4.5" stroke="var(--orange)" fill="none"/></svg>info@bruntel.ph</p>
  </div>
  <div class="abs col" style="left:609px;top:50px;width:150px">
    <h5>Satellite Office</h5>
    <p><svg width="10" height="12" viewBox="0 0 10 12"><path d="M5 11S1 7 1 4.5a4 4 0 0 1 8 0C9 7 5 11 5 11z" stroke="var(--orange)" fill="none"/><circle cx="5" cy="4.5" r="1.3" fill="var(--orange)"/></svg>Purok Dalisay, Brgy. Malinta Rosales City, Batangas Philippines 4210</p>
    <p><svg width="11" height="11" viewBox="0 0 11 11"><path d="M2 1l2 .2.8 2.3-1.2 1a6 6 0 0 0 3 3l1-1.2 2.3.8.1 2C7 10 1 4 2 1z" stroke="var(--orange)" fill="none"/></svg>+63 (0) 43 555-0182</p>
    <p><svg width="12" height="10" viewBox="0 0 12 10"><rect x=".5" y=".5" width="11" height="9" stroke="var(--orange)" fill="none"/><path d="M.5 .5L6 5l5.5-4.5" stroke="var(--orange)" fill="none"/></svg>info@bruntel.ph</p>
  </div>
  <div class="abs badge" style="left:813px;top:50px"><i></i></div>
  <div class="abs badge" style="left:912px;top:50px"><i></i></div>
  <div class="abs badge" style="left:813px;top:127px"><i></i></div>
  <div class="abs" style="left:0;top:244px;width:1200px;height:1px;background:#444"></div>
</footer>
<div class="abs copy">© 2026 <span style="color:var(--orange);text-decoration:underline">Bruntel</span> All Rights Reserved</div>

</body>
</html>
```